Glass window Vinyl

We are in need of window vinyls for the building shown in the photos. The current vinyls will come down, and we will install the new signage created by this process. We need to advertise:

"Harwell's Landing Pop Up Market"

Then, below that, it should say for rental inquiries call : 555.613.0872 with our logo which is attached along with our colors and brand guidelines. You may add more color to the Harwells landing pop up market signage if appropriate. It should be large enough to be easily read from the road by those passing by.

```html
<!DOCTYPE html>
<html lang="en">
<head>
<meta charset="utf-8">
<title>Harwell's Landing Pop Up Market – Window Vinyl</title>
<link rel="stylesheet" href="https://fonts.googleapis.com/css2?family=Marcellus&family=Montserrat:wght@400;500;700&display=swap">
<style>
  :root {
    --teal: #12404f;
    --gold: #b59e6b;
    --white: #ffffff;
    --canvas: #ffffff;
  }
  * { margin: 0; padding: 0; box-sizing: border-box; }
  html, body {
    width: 1092px; height: 1200px; overflow: hidden;
    background: var(--canvas);
  }
  .canvas { position: relative; width: 1092px; height: 1200px; }
  .sign {
    position: absolute; left: 135px; top: 129px;
    width: 815px; height: 934px;
    background: var(--teal);
    box-shadow: 10px 12px 22px rgba(0,0,0,0.35);
  }
  .sign-frame { position: absolute; left: 0; top: 0; }
  .centered {
    position: absolute; left: 0; width: 815px;
    text-align: center; white-space: nowrap;
  }
  .brand-name {
    top: 150px;
    font-family: "Marcellus", serif;
    font-size: 42px; letter-spacing: 7px;
    color: var(--white);
  }
  .brand-tagline {
    top: 222px;
    font-family: "Montserrat", sans-serif;
    font-weight: 700; font-size: 18px; letter-spacing: 7px;
    color: var(--gold);
  }
  .headline {
    font-family: "Marcellus", serif;
    color: var(--white);
    font-size: 80px; line-height: 1;
  }
  .headline-1 { top: 332px; }
  .headline-2 { top: 423px; }
  .headline-sub {
    top: 522px;
    font-family: "Montserrat", sans-serif;
    font-weight: 400; font-size: 58px; line-height: 1;
    color: var(--teal);
  }
  .inquiry {
    top: 669px;
    font-family: "Montserrat", sans-serif;
    font-weight: 700; font-size: 40px; line-height: 1;
    color: var(--gold);
  }
  .call-row {
    position: absolute; left: 110px; top: 752px;
    display: flex; align-items: center; gap: 22px;
  }
  .call-badge {
    width: 126px; height: 56px; border-radius: 7px;
    background: var(--gold); color: var(--teal);
    font-family: "Montserrat", sans-serif; font-weight: 700; font-size: 26px;
    display: flex; align-items: center; justify-content: center;
  }
  .phone {
    font-family: "Marcellus", serif;
    font-size: 72px; line-height: 1; color: var(--white);
    letter-spacing: 1px;
  }
  .website {
    top: 855px;
    font-family: "Montserrat", sans-serif;
    font-weight: 500; font-size: 21px;
    color: var(--gold);
  }
</style>
</head>
<body>
<div class="canvas">
  <div class="sign">
    <svg class="sign-frame" width="815" height="934" viewBox="0 0 815 934" aria-hidden="true">
      <rect x="21.5" y="21.5" width="772" height="891" fill="none" stroke="#b59e6b" stroke-width="3"/>
      <rect x="20" y="298" width="775" height="314" fill="#b59e6b"/>
      <g stroke="#b59e6b" stroke-width="1.5">
        <line x1="47" y1="137" x2="47" y2="298"/>
        <line x1="70" y1="202" x2="70" y2="298"/>
        <line x1="745" y1="52" x2="745" y2="298"/>
        <line x1="768" y1="52" x2="768" y2="298"/>
        <line x1="47" y1="612" x2="47" y2="883"/>
        <line x1="70" y1="612" x2="70" y2="883"/>
        <line x1="745" y1="612" x2="745" y2="731"/>
        <line x1="768" y1="612" x2="768" y2="796"/>
      </g>
    </svg>

    <div class="centered brand-name">WILLOW CREST</div>
    <div class="centered brand-tagline">PROPERTIES</div>

    <div class="centered headline headline-1">HARWELL'S</div>
    <div class="centered headline headline-2">LANDING</div>
    <div class="centered headline-sub">POP UP MARKET</div>

    <div class="centered inquiry">FOR RENTAL INQUIRIES</div>
    <div class="call-row">
      <span class="call-badge">CALL</span>
      <span class="phone">555.613.0872</span>
    </div>
    <div class="centered website">www.willowcrestproperties.com</div>
  </div>
</div>
</body>
</html>
```